Business Cards for IT Consulting Company (Managed Service Provider)

I am looking to have some business cards printed and would like some designs. We are an IT Consulting company based in Vancouver BC. I would like a nice clean and modern look to the cards. I have uploaded all the versions of my logo so parts can be used as needed. Here is a snippit from our website homepage:

Kelbrin Systems Ltd. is an IT Solutions Partner located in Vancouver BC, Canada. We offer IT solutions and support to customers in the greater Vancouver Area. With expertise in Quillara platforms, as well as Tovex and Bryn ZPL and over 12 years experience in the IT industry, Kelbrin Systems is dedicated to offering our clients top quality service and products. We take pride in the solutions we offer our customers. The greatest compliment a client can give us is to recommend our services.

Kelbrin Systems Ltd. offers a wide range of IT services from onsite service to remote support and managed service solutions. This allows clients to choose the support path that best suits their company’s needs. Supporting many different sized companies from small to enterprise level over the past 12 years Kelbrin Systems has the experience and expertise needed to ensure things run smoothly. Allowing our clients to focus on doing business.

Revolutionizing the way IT services are delivered.

Kelbrin Systems is dedicated to providing our clients with IT solutions that work and grow with them for years to come. This philosophy helps save money in the long run instead of replacing equipment constantly. Far too often IT solutions are not well thought out and while possibly solving the problem at hand, require replacement due to growth or quality within a very short time frame. Kelbrin Systems takes pride in providing solutions that will last and be able to accommodate growth without the need for replacement.

Industry/Entity Type

Information Technology

Contact Information for Business Card

Kelbrin Systems Ltd.
(Employee Name)
Eml: (Employees Email Address)
Web: kelbrinsys.me
Ph: 604-555-0142

Font styles to use
Serif
Sans Serif

Requirements
Must have
• The Company logo and company colors.
Nice to have
• - Our tag line: "Revolutionizing IT Services" or "Revolutionizing the way IT services are delivered."
• - Also I really like the idea of nature and technology together blending which is sort of where my logo came from so integrating that somehow onto the business cards would be great.

```html
<!DOCTYPE html>
<html lang="en">
<head>
<meta charset="utf-8">
<title>Kelbrin Systems Ltd. — Business Cards</title>
<link rel="stylesheet" href="https://fonts.googleapis.com/css2?family=Montserrat:wght@400;500;600&display=swap">
<style>
  :root {
    --backdrop: #2d2d2d;
    --card: #ffffff;
    --brand-blue: #2f9fde;
    --brand-blue-faint: #c6dcf0;
    --ink: #2b2b2b;
    --ink-soft: #555555;
  }
  * { box-sizing: border-box; margin: 0; padding: 0; }
  html, body {
    width: 1200px; height: 1114px; overflow: hidden;
    background: var(--backdrop);
    font-family: "Montserrat", sans-serif;
  }
  .canvas {
    position: relative; width: 1200px; height: 1114px;
  }
  .card {
    position: absolute; left: 180px; width: 840px; height: 480px;
    background: var(--card);
    box-shadow: 0 10px 30px rgba(0,0,0,.45);
    overflow: hidden;
  }
  .card--front { top: 60px; }
  .card--back { top: 574px; }

  .brand {
    display: flex; align-items: center; gap: 18px;
    color: var(--brand-blue);
    font-weight: 600;
  }
  .brand__dot {
    width: 54px; height: 54px; border-radius: 50%;
    background: var(--brand-blue);
    flex: none;
  }
  .brand__name { font-size: 44px; line-height: 1; letter-spacing: -0.5px; }

  .card--front .brand {
    position: absolute; left: 50%; top: 170px; transform: translateX(-50%);
    white-space: nowrap;
  }
  .tagline {
    position: absolute; left: 0; right: 0; bottom: 64px;
    text-align: center; font-size: 20px; letter-spacing: 0.6px;
    color: var(--ink);
  }

  .card--back .brand { position: absolute; left: 60px; top: 70px; }
  .card--back .brand__name { font-size: 38px; }
  .card--back .brand__dot { width: 44px; height: 44px; }

  .backdrop-mark {
    position: absolute; right: -70px; top: 40px;
    width: 360px; height: 360px; border-radius: 50%;
    border: 14px solid var(--brand-blue-faint);
  }

  .contact { position: absolute; left: 150px; bottom: 56px; color: var(--ink); }
  .contact__name { color: var(--brand-blue); font-weight: 600; font-size: 24px; }
  .contact__role { font-size: 20px; margin-bottom: 22px; color: var(--ink-soft); }
  .contact__list { list-style: none; }
  .contact__item {
    display: flex; align-items: center; gap: 14px;
    font-size: 22px; line-height: 36px;
  }
  .contact__icon { width: 20px; height: 20px; flex: none; color: var(--brand-blue); }
</style>
</head>
<body>
<main class="canvas">
  <section class="card card--front" aria-label="Card front">
    <div class="brand">
      <span class="brand__dot" aria-hidden="true"></span>
      <span class="brand__name">Kelbrin Systems Ltd.</span>
    </div>
    <p class="tagline">Revolutionizing the way IT services are delivered</p>
  </section>

  <section class="card card--back" aria-label="Card back">
    <div class="backdrop-mark" aria-hidden="true"></div>
    <div class="brand">
      <span class="brand__dot" aria-hidden="true"></span>
      <span class="brand__name">Kelbrin Systems Ltd.</span>
    </div>
    <div class="contact">
      <p class="contact__name">Daniel Marsh</p>
      <p class="contact__role">Network Engineer</p>
      <ul class="contact__list">
        <li class="contact__item">
          <svg class="contact__icon" viewBox="0 0 24 24" aria-hidden="true"><path fill="currentColor" d="M6.6 10.8a15.1 15.1 0 0 0 6.6 6.6l2.2-2.2c.3-.3.7-.4 1-.2 1.1.4 2.3.6 3.6.6.6 0 1 .4 1 1V20c0 .6-.4 1-1 1A17 17 0 0 1 3 4c0-.6.4-1 1-1h3.5c.6 0 1 .4 1 1 0 1.3.2 2.5.6 3.6.1.3 0 .7-.2 1z"/></svg>
          <span>604-555-0142</span>
        </li>
        <li class="contact__item">
          <svg class="contact__icon" viewBox="0 0 24 24" aria-hidden="true"><path fill="currentColor" d="M2 5h20v14H2zm2 2v.5l8 5 8-5V7zm0 2.8V17h16V9.8l-8 5z"/></svg>
          <span>dmarsh@kelbrinsys.me</span>
        </li>
        <li class="contact__item">
          <svg class="contact__icon" viewBox="0 0 24 24" aria-hidden="true"><g fill="none" stroke="currentColor" stroke-width="1.8"><circle cx="12" cy="12" r="9.5"/><ellipse cx="12" cy="12" rx="4.2" ry="9.5"/><path d="M2.5 12h19M4 7h16M4 17h16"/></g></svg>
          <span>www.kelbrinsys.me</span>
        </li>
      </ul>
    </div>
  </section>
</main>
</body>
</html>
```